Personal Injury Law Firm Marketing Postcards

Looking for 4 different high quality graphic postcards (print on both sides of 4"x6" postcard to market a Personal Injury Lawyer (Walter Dunmore). These will be placed on cars and in stores on stands. My photo and/or stock images.... We are targeting People who have been injured in automobile accidents, motorcycle accidents, slip and fall (wet/greasy floors indoors in supermarkets, restaurants, etc., snow and ice outdoors on sidewalks) trip and fall cases on dangerous staircases. indoor/outdoor, dog bite injuries. ( I like the use of stock images of these type of injury causing accidents. You can use following language "Serving People Injured in NY & NJ" . Millions of Dollars Recovered, Free Consultation and No Fee Unless We Recover Money! Phone number to be displayed (555) 614-3082 "call or text" Available 24 hours a day 7 days per week. May also want to mention that we can take over your case from another lawyer if you are not satisfied with your current attorney. There should be a small space in corner which has a space for my marketing person to handwrite in their reference code.

Target Market(s)

18-75 years old - densely populated major city

Industry/Entity Type

Legal

Font styles to use
Other font styles liked:
• Please use logo style that I uploaded.. Please do not just cut parts of my website out and use them. Do not use LOGO from my website

Colors
0054AA
0677BA
7BADD7
CADEEF
E8F1F8
00AB8E
00BBA5
67D7C9
C6EFE9
E9F9F6

Requirements
Must have
• Professional Appearance

```html
<!DOCTYPE html>
<html lang="en">
<head>
<meta charset="utf-8">
<title>Walter Dunmore – Personal Injury Postcard</title>
<link rel="stylesheet" href="https://fonts.googleapis.com/css2?family=Noto+Serif:wght@700&family=Poppins:wght@400;500;600;700&display=swap">
<style>
  :root{
    --stage:#a6a6a6;
    --navy:#0b2a52;
    --navy-deep:#081f3f;
    --blue:#0d4f8f;
    --blue-bright:#0a6cb8;
    --gold:#cfae62;
    --white:#ffffff;
    --ink:#0f2a4f;
    --stamp:#a0a2a6;
  }
  *{box-sizing:border-box;margin:0;padding:0}
  html,body{width:1200px;height:1117px;overflow:hidden}
  body{background:var(--stage);font-family:"Poppins",sans-serif;position:relative}

  .card{position:absolute;left:235px;width:729px;height:486px;overflow:hidden;background:var(--white)}
  .card--front{top:57px}
  .card--back{top:569px}

  /* FRONT */
  .hero{position:absolute;left:0;top:0;width:729px;height:283px;
    background:linear-gradient(100deg,var(--navy-deep) 0%,var(--navy) 30%,var(--blue) 60%,#0f3a6e 80%,#0b2c58 100%)}
  .photo{position:absolute}
  .photo--accident{left:0;top:283px;width:300px;height:187px;
    background:linear-gradient(135deg,#8f8680 0%,#5c5a5c 45%,#2f3136 100%)}
  .photo--dog{left:520px;top:283px;width:209px;height:187px;
    background:linear-gradient(135deg,#4f6a3c 0%,#b28a58 45%,#3b4a6e 100%)}
  .photo--lawyer{left:272px;top:0;width:288px;height:470px;
    background:linear-gradient(180deg,#1a2b45 0%,#3a3f4c 40%,#1f2430 100%)}

  .headline{position:absolute;left:45px;top:26px;font-family:"Noto Serif",serif;font-weight:700;
    font-size:33px;line-height:34.5px;color:var(--white);letter-spacing:-.3px;text-transform:uppercase}
  .headline .accent{color:var(--gold)}
  .promise{position:absolute;left:45px;top:214px;font-size:13px;line-height:15.6px;color:var(--white);font-weight:500}

  .firm-name{position:absolute;color:var(--gold);font-weight:500;text-transform:uppercase;line-height:1.05;text-align:center;white-space:nowrap}
  .card--front .firm-name{left:524px;top:122px;width:190px;font-size:18px}

  .contact-bar{position:absolute;left:0;top:438px;width:729px;height:48px}
  .contact-bar svg{position:absolute;left:0;top:0}
  .contact-list{position:absolute;left:132px;top:446px;height:18px;display:flex;align-items:center;gap:9px;
    font-size:12px;font-weight:600;color:var(--ink);white-space:nowrap}
  .contact-list .sep{width:1.5px;height:20px;background:var(--ink)}
  .contact-item{display:flex;align-items:center;gap:6px}
  .dot-icon{width:13px;height:13px;border-radius:50%;background:var(--blue-bright);display:inline-block}

  /* BACK */
  .back-bg{position:absolute;inset:0;background:linear-gradient(160deg,#ffffff 45%,#f1f2f4 75%,#e9eaec 100%)}
  .back-shapes{position:absolute;left:0;top:0}
  .card--back .firm-name{left:369px;top:74px;width:150px;font-size:12px}
  .stamp-box{position:absolute;left:624px;top:23px;width:77px;height:77px;background:var(--stamp)}

  .services{position:absolute;left:36px;top:226px;display:grid;grid-template-columns:97px 97px 110px;row-gap:10px}
  .service{display:flex;align-items:center;gap:6px;height:35px}
  .service .ring{flex:none;width:34px;height:34px;border-radius:50%;background:var(--white);border:3px solid var(--gold)}
  .service span{font-size:6.8px;line-height:8.6px;color:var(--white);text-transform:uppercase;font-weight:500}

  .cta{position:absolute;left:42px;top:384px;color:var(--white);white-space:nowrap}
  .cta-lead{font-size:12.2px;line-height:14px;font-weight:700}
  .cta-phone{display:flex;align-items:center;gap:8px;margin-top:5px}
  .cta-phone .phone-dot{width:31px;height:31px;border-radius:50%;background:var(--gold);display:flex;align-items:center;justify-content:center}
  .cta-phone strong{font-size:29px;font-weight:700;line-height:34px;letter-spacing:.2px}
  .cta-links{display:flex;align-items:center;gap:8px;margin-top:2px;font-size:11.5px;line-height:14px}
  .cta-links .sep{width:1.2px;height:14px;background:var(--gold)}
  .cta-links .gold-dot{width:10px;height:10px;border-radius:50%;background:var(--gold);display:inline-block;margin-right:5px;vertical-align:-1px}
</style>
</head>
<body>

<section class="card card--front">
  <div class="hero"></div>
  <div class="photo photo--accident" role="img" aria-label="Rescue crew at an overturned car accident scene"></div>
  <div class="photo photo--dog" role="img" aria-label="Dog biting a person's arm"></div>
  <div class="photo photo--lawyer" role="img" aria-label="Portrait of the attorney in a suit"></div>

  <h1 class="headline"><span class="accent">Personal<br>Injury Lawyer</span><br>Serves all of<br>New Jersey and<br>New York.</h1>
  <p class="promise">Millions of Dollars Recovered,<br>Free Consultation and No Fee Unless<br>We Recover Money!</p>

  <div class="firm-name">Law Office of<br>Walter Dunmore</div>

  <div class="contact-bar">
    <svg width="729" height="48" viewBox="0 0 729 48">
      <polygon points="0,32 729,32 729,48 0,48" fill="#ffffff"/>
      <polygon points="115,0 634,0 650,32 98,32" fill="#ffffff"/>
    </svg>
  </div>
  <div class="contact-list">
    <span class="contact-item"><i class="dot-icon"></i>www.wdlegal.com</span>
    <span class="sep"></span>
    <span class="contact-item"><i class="dot-icon"></i>wdunmore@wdlegal.com</span>
    <span class="sep"></span>
    <span class="contact-item">
      <svg width="13" height="13" viewBox="0 0 24 24"><circle cx="12" cy="12" r="12" fill="#0a6cb8"/><path d="M8.5 6.5l2 2.2-1.2 1.5c.8 1.7 2 2.9 3.6 3.7l1.4-1.2 2.2 2-1 1.8c-3.8-.4-7.6-4.2-8-8z" fill="#fff"/></svg>
      (555) 614-3082</span>
  </div>
</section>

<section class="card card--back">
  <div class="back-bg"></div>
  <svg class="back-shapes" width="729" height="486" viewBox="0 0 729 486">
    <polygon points="0,208 352,208 374,170 366,367 0,367" fill="#0b2a52"/>
    <polygon points="0,367 303,367 371,486 0,486" fill="#0a6cb8"/>
    <polygon points="0,203 348,203 390,95 346,0 0,0" fill="#ffffff"/>
  </svg>
  <div class="photo" style="left:0;top:0;width:386px;height:207px;clip-path:polygon(0 0,341px 0,386px 95px,345px 203px,0 203px);background:linear-gradient(135deg,#b9bcc2 0%,#2e3d66 50%,#c9483a 80%,#f0c419 100%)" role="img" aria-label="Injured worker sitting on a warehouse floor beside a yellow hard hat"></div>

  <div class="firm-name">Law Office of<br>Walter Dunmore</div>
  <div class="stamp-box"></div>

  <div class="services">
    <div class="service"><i class="ring"></i><span>Dog bites /<br>attacks</span></div>
    <div class="service"><i class="ring"></i><span>Trip and fall<br>accidents</span></div>
    <div class="service"><i class="ring"></i><span>Wrongful<br>death attorneys</span></div>
    <div class="service"><i class="ring"></i><span>Workplace<br>accidents</span></div>
    <div class="service"><i class="ring"></i><span>Truck<br>accidents</span></div>
    <div class="service"><i class="ring"></i><span>Slip and<br>fall accidents</span></div>
    <div class="service"><i class="ring"></i><span>Motorcycle<br>accidents</span></div>
    <div class="service"><i class="ring"></i><span>Pedestrian<br>accidents</span></div>
    <div class="service"><i class="ring"></i><span>Car<br>accidents</span></div>
  </div>

  <div class="cta">
    <p class="cta-lead">call or text Available 24 hours a day<br>7 days per week.</p>
    <div class="cta-phone">
      <span class="phone-dot"><svg width="17" height="17" viewBox="0 0 24 24"><path d="M6 3l3.5 4-2 2.4c1.3 2.8 3.3 4.8 6.1 6.1l2.4-2 4 3.5-1.7 3C10.5 19.3 4.7 13.5 3 5.7z" fill="#0a6cb8"/></svg></span>
      <strong>(555) 614-3082</strong>
    </div>
    <div class="cta-links">
      <span><i class="gold-dot"></i>www.wdlegal.com</span>
      <span class="sep"></span>
      <span><i class="gold-dot"></i>wdunmore@wdlegal.com</span>
    </div>
  </div>
</section>

</body>
</html>
```